Marn-ridge Tide Harbor Custom Brokers Limited

Name: Dorvella Hastings
Title: Customs Broker
Address: Shop 9 Birchfield Commercial Complex
207-209 Harlow Road
Kingston 8
Telephone: (876)
Email: tideharborport@quillmail.example

```html
<!DOCTYPE html>
<html lang="en">
<head>
<meta charset="utf-8">
<title>Marn-ridge Tide Harbor Custom Brokers Limited — Business Card</title>
<link href="https://fonts.googleapis.com/css2?family=Montserrat:wght@400;500;600;700&display=swap" rel="stylesheet">
<style>
  :root {
    --navy: #1d3d63;
    --gold: #e2a91c;
    --paper: #f7f7f6;
    --ink: #1f2a3a;
    --backdrop: #e4e5e7;
    --faint: #ebecec;
  }
  * { box-sizing: border-box; margin: 0; padding: 0; }
  html, body { width: 1200px; height: 794px; overflow: hidden; }
  body {
    background: var(--backdrop);
    font-family: "Montserrat", sans-serif;
    position: relative;
  }
  .card {
    position: absolute;
    width: 540px;
    height: 309px;
    overflow: hidden;
    box-shadow: 0 6px 18px rgba(0,0,0,0.12);
  }
  .card::after {
    content: "";
    position: absolute;
    left: 0; right: 0; bottom: 0;
    height: 12px;
    background: var(--gold);
  }
  .card--front { left: 50px; top: 120px; background: var(--navy); }
  .card--back { left: 610px; top: 365px; background: var(--paper); }

  .brand {
    display: flex;
    align-items: center;
    gap: 12px;
  }
  .brand__dot { flex: none; border-radius: 50%; }
  .brand__name {
    font-weight: 600;
    line-height: 1.25;
    letter-spacing: 0.02em;
  }

  .card--front .brand {
    position: absolute;
    left: 0; right: 0; top: 112px;
    justify-content: center;
  }
  .card--front .brand__dot { width: 46px; height: 46px; background: var(--gold); }
  .card--front .brand__name { color: #fff; font-size: 19px; }

  .back__mark {
    position: absolute;
    right: -40px; top: -40px;
    width: 220px; height: 220px;
    border-radius: 50%;
    background: var(--faint);
  }
  .card--back .brand { position: absolute; left: 34px; top: 40px; }
  .card--back .brand__dot { width: 30px; height: 30px; background: var(--navy); }
  .card--back .brand__name { color: var(--navy); font-size: 13px; }

  .back__rule {
    position: absolute;
    left: 240px; right: 30px; top: 150px;
    height: 1.5px;
    background: var(--gold);
  }
  .person { position: absolute; left: 34px; top: 158px; }
  .person__name { color: var(--navy); font-weight: 700; font-size: 15px; letter-spacing: 0.02em; }
  .person__title { color: var(--ink); font-weight: 500; font-size: 13px; margin-top: 3px; }

  .contact { position: absolute; left: 34px; top: 222px; list-style: none; }
  .contact__item {
    display: flex; align-items: center; gap: 10px;
    color: var(--ink); font-size: 12.5px; margin-bottom: 8px;
  }
  .contact__icon { width: 14px; height: 14px; flex: none; }

  .address {
    position: absolute; right: 30px; top: 162px;
    text-align: right;
    color: var(--ink); font-size: 12px; line-height: 1.6;
    font-style: normal;
  }
</style>
</head>
<body>

<section class="card card--front" aria-label="Card front">
  <div class="brand">
    <span class="brand__dot"></span>
    <span class="brand__name">Marn-ridge Tide Harbor<br>Custom Brokers Limited</span>
  </div>
</section>

<section class="card card--back" aria-label="Card back">
  <div class="back__mark"></div>
  <div class="brand">
    <span class="brand__dot"></span>
    <span class="brand__name">Marn-ridge Tide Harbor<br>Custom Brokers Limited</span>
  </div>

  <div class="back__rule"></div>

  <div class="person">
    <p class="person__name">DORVELLA HASTINGS</p>
    <p class="person__title">Customs Broker</p>
  </div>

  <ul class="contact">
    <li class="contact__item">
      <svg class="contact__icon" viewBox="0 0 24 24" fill="none" stroke="var(--gold)" stroke-width="2" stroke-linecap="round" stroke-linejoin="round"><path d="M5 3h4l2 5-3 2a11 11 0 0 0 6 6l2-3 5 2v4a2 2 0 0 1-2 2A17 17 0 0 1 3 5a2 2 0 0 1 2-2z"/></svg>
      (876) 555-0142
    </li>
    <li class="contact__item">
      <svg class="contact__icon" viewBox="0 0 24 24" fill="none" stroke="var(--gold)" stroke-width="2" stroke-linejoin="round"><rect x="2" y="5" width="20" height="14" rx="1"/><path d="M2 6l10 7 10-7"/></svg>
      tideharborport@quillmail.example
    </li>
  </ul>

  <address class="address">
    Shop 9 Birchfield Commercial Complex<br>
    207-209 Harlow Road, Kingston 8
  </address>
</section>

</body>
</html>
```